Bright Robin Pet Sitting Postcard

I will be sending these postcards to homes in the neighborhood introducing my pet sitting business.

Include the following on the postcard:
Rosalind Mabry
738-405-2917
www.brightrobinpetsitting.example
help@brightrobinpetsitting.example

```html
<!DOCTYPE html>
<html lang="en">
<head>
<meta charset="utf-8">
<title>Bright Robin Pet Sitting Postcard</title>
<link rel="stylesheet" href="https://fonts.googleapis.com/css2?family=Quicksand:wght@400;500;600&display=swap">
<style>
  :root {
    --teal: #1cb3c1;
    --white: #ffffff;
    --ink: #111111;
    --orange: #f2a414;
    --orange-deep: #f07f1a;
    --red: #e31b3b;
    --blue: #1f6fb8;
    --air-blue: #a6d8e8;
    --rule: #a9c9ea;
    --divider: #8fb8e0;
  }
  * { box-sizing: border-box; margin: 0; padding: 0; }
  html, body { width: 1200px; height: 1200px; overflow: hidden; }
  body {
    background: var(--teal);
    position: relative;
    font-family: "Quicksand", sans-serif;
  }

  /* Front card */
  .card-front {
    position: absolute;
    left: 191px; top: 70px;
    width: 795px; height: 484px;
    background: var(--white);
  }
  .brand-ring {
    position: absolute;
    border: 6px solid var(--ink);
    border-radius: 50%;
  }
  .card-front .brand-ring {
    left: 272px; top: 128px; width: 240px; height: 240px;
  }
  .brand-name {
    position: absolute;
    left: 0; width: 100%;
    text-align: center;
    color: var(--ink);
    font-weight: 500;
  }
  .card-front .brand-name { top: 392px; font-size: 36px; }

  /* Back card (postcard) */
  .card-back {
    position: absolute;
    left: 310px; top: 585px;
    width: 720px; height: 510px;
    background: repeating-linear-gradient(135deg,
      var(--air-blue) 0 46px, var(--red) 46px 58px);
  }
  .card-back-inner {
    position: absolute;
    left: 29px; top: 25px;
    width: 661px; height: 460px;
    background: var(--white);
  }
  .card-back .brand-ring {
    left: 104px; top: 150px; width: 150px; height: 150px;
  }
  .card-back .brand-name {
    top: 318px; width: 310px; font-size: 22px;
  }
  .divider {
    position: absolute;
    left: 311px; top: 26px;
    width: 2px; height: 408px;
    background: var(--divider);
  }
  .stamp {
    position: absolute;
    left: 527px; top: 28px;
    width: 100px; height: 106px;
    border-radius: 4px;
    background: linear-gradient(180deg, var(--orange) 0%, var(--orange-deep) 100%);
  }
  .details {
    position: absolute;
    left: 323px; top: 164px;
    width: 302px;
    text-align: center;
    list-style: none;
  }
  .details li { border-bottom: 2px solid var(--rule); }
  .tagline {
    color: var(--orange);
    font-size: 22px; line-height: 23px;
    padding-bottom: 6px;
    letter-spacing: 0.5px;
  }
  .call {
    color: var(--orange);
    font-size: 22px; line-height: 38px;
    letter-spacing: 0.5px;
  }
  .owner {
    color: var(--red);
    font-size: 26px; line-height: 42px;
    letter-spacing: 1px;
  }
  .phone {
    color: var(--red);
    font-size: 25px; line-height: 40px;
    letter-spacing: 1px;
  }
  .email, .web {
    color: var(--blue);
    font-size: 16.5px; line-height: 40px;
    font-weight: 500;
  }
  .details li.credentials {
    border-bottom: none;
    color: var(--blue);
    font-size: 15px; line-height: 34px;
    letter-spacing: 0.5px;
  }
</style>
</head>
<body>

  <section class="card-front">
    <div class="brand-ring"></div>
    <p class="brand-name">Bright Robin Pet Sitting</p>
  </section>

  <section class="card-back">
    <div class="card-back-inner">
      <div class="brand-ring"></div>
      <p class="brand-name">Bright Robin Pet Sitting</p>

      <div class="divider"></div>

      <div class="stamp" role="img" aria-label="Postage stamp area with dog and cat illustration"></div>

      <ul class="details">
        <li class="tagline">PETS HOME ALONE?<br>I CAN HELP!</li>
        <li class="call">CALL ME TODAY</li>
        <li class="owner">ROSALIND MABRY</li>
        <li class="phone">738•405•2917</li>
        <li class="email">help@brightrobinpetsitting.example</li>
        <li class="web">www.brightrobinpetsitting.example</li>
        <li class="credentials">Certified, Insured &amp; Bonded</li>
      </ul>
    </div>
  </section>

</body>
</html>
```